Up to the Challenge? Canadian based consulting company needs a two sided business card design

A Canadian based security risk management consulting company needs a two-sided business card design. What we do is provide advice and guidance related to emergency, security and business continuity management for small, medium and large companies to help ensure the protection of their people, assets, information, services, operations and reputation.

The final design should be simple, only one or two colours, eye catching, professional and one that makes people look at three or more times just because it looks so darn good.

I have include examples of business cards I like.

Target Market(s)

Small, medium and large companies.

Industry/Entity Type

Security

Contact Information for Business Card

Business Card Size: Standard size of 3.5" (89mm) x 2.0" (51mm) - (see full specifications and guides on PRINTA's website if required)
Card Stock: Looking to use PRINTA's Velda 32pt stock textured paper - seam colour either chili red or black
Business Name: The Harrowfield Group
Website: www.theharrowfieldgroup.example
Telephone: (555)214-0397
Name: Dana Forsythe
Position: Principle
e-mail: Dana.Forsythe@theharrowfieldgroup.example

Font styles to use
Serif

Colors
ec1f27
000000
9d9d9d
aaaaaa
606060

Requirements
Must have
• - "The Harrowfield Group" logo (see uploaded files). I have included grey scale and colour versions.
• - Business card details (as above)
Nice to have
• - One side black or grey scale.
• - Other side would likely be white.
• - Everyone likes the silver logo on the black background.
• - Small element of colour i.e. red but I'm leaning more to greyscale.
Should not have
• - A lot of colour. Keep it simple.

```html
<!DOCTYPE html>
<html lang="en">
<head>
<meta charset="utf-8">
<title>The Harrowfield Group — Business Card</title>
<link rel="stylesheet" href="https://fonts.googleapis.com/css2?family=Noto+Serif:wght@400;700&display=swap">
<style>
  :root {
    --stage: #3a3a36;
    --card: #121212;
    --card-edge: #1c1c1c;
    --silver: #9d9d9d;
    --silver-light: #aaaaaa;
    --ink-white: #f4f4f4;
    --contact: #d6d6d6;
  }
  * { margin: 0; padding: 0; box-sizing: border-box; }
  html, body {
    width: 1200px;
    height: 900px;
    overflow: hidden;
    background: var(--stage);
    font-family: "Noto Serif", Georgia, serif;
  }
  .canvas {
    position: relative;
    width: 1200px;
    height: 900px;
    display: flex;
    align-items: center;
    justify-content: center;
    gap: 40px;
  }
  .card {
    position: relative;
    width: 540px;
    height: 309px;
    background: linear-gradient(160deg, var(--card-edge) 0%, var(--card) 60%);
    border-radius: 4px;
    box-shadow: 0 10px 28px rgba(0,0,0,0.45);
  }
  .card-front { padding: 70px 0 0 70px; }
  .brand {
    display: flex;
    align-items: center;
    gap: 16px;
  }
  .brand-name {
    color: var(--silver);
    font-weight: 400;
    font-size: 25px;
    letter-spacing: 1.5px;
    line-height: 1.2;
    text-transform: uppercase;
  }
  .brand-mark {
    width: 44px;
    height: 44px;
    border-radius: 50%;
    background: var(--silver);
  }
  .holder-name {
    margin-top: 34px;
    color: var(--ink-white);
    font-weight: 700;
    font-size: 30px;
    letter-spacing: 1px;
    text-transform: uppercase;
  }
  .holder-title {
    margin-top: 6px;
    color: var(--contact);
    font-size: 15px;
    letter-spacing: 1px;
    text-transform: uppercase;
  }
  .card-back {
    display: flex;
    align-items: center;
    justify-content: center;
  }
  .contact-list {
    list-style: none;
    text-align: center;
    color: var(--contact);
    font-size: 17px;
    line-height: 1.55;
  }
</style>
</head>
<body>
  <main class="canvas">
    <section class="card card-front" aria-label="Card front">
      <div class="brand">
        <span class="brand-name">The Harrowfield<br>Group</span>
        <span class="brand-mark" aria-hidden="true"></span>
      </div>
      <p class="holder-name">Dana Forsythe</p>
      <p class="holder-title">Principle</p>
    </section>
    <section class="card card-back" aria-label="Card back">
      <ul class="contact-list">
        <li>P: (555)214-0397</li>
        <li>E: dana.forsythe@theharrowfieldgroup.example</li>
        <li>W: www.theharrowfieldgroup.example</li>
      </ul>
    </section>
  </main>
</body>
</html>
```